Lift-Lantern needs a design for a new mobile app

A new app - lift-lantern.example, requires a design for its new app.

The app lets users add, create and share gym sessions. Sessions can be created, sets added and exercises chosen.

The app is currently functional on Android only (ios later), all that is required is a design for the app.

Some design assets are available (logo, colours, font), so the app should tie into these.

The design needs to be clean, simple and obvious, and all design assets will be required as part of this project.

One of the pages has % complete on the set - an icon to demonstrate this rather than a text based (eg 50%) would be great.

Screenshots will be available, along with the logos, colours and fonts.

Target Market(s)

Gym goers, all ages, male & female, fitness enthusiasts
Users of phones and tablets

Industry/Entity Type

Gym

Requirements
Must have
• Designs examples for each of the screens in the app, and an obvious selection of reusable elements (such as drop downs, radio buttons, buttons, calendar selectors, check boxes etc)
• Colours, logos and branding to fit into what is already available on the website.
• Usability and consistency are vital. Buttons should be in the same place (where possible).
• Design should help the user to complete the journey, and not get in the way.
• It should be a pleasure to use the app.
• Happy to have white space where appropriate.
• We use native elements where available.
Should not have
• Design features that waste space

```html
<!DOCTYPE html>
<html lang="en">
<head>
<meta charset="utf-8">
<title>Lift-Lantern — Notifications</title>
<link rel="stylesheet" href="https://fonts.googleapis.com/css2?family=Roboto:wght@400;500;700&display=swap">
<style>
  :root {
    --status-bar: #5169cf;
    --app-bar: #5d77d6;
    --on-primary: #ffffff;
    --surface: #ffffff;
    --text-unread: #1b1b1b;
    --text-read: #8a8a8a;
    --text-time: #8c8c8c;
  }
  * { margin: 0; padding: 0; box-sizing: border-box; }
  html, body {
    width: 675px;
    height: 1200px;
    overflow: hidden;
    background: var(--surface);
    font-family: "Roboto", Arial, sans-serif;
  }
  .screen {
    position: relative;
    width: 675px;
    height: 1200px;
    background: var(--surface);
  }
  .status-bar {
    height: 45px;
    background: var(--status-bar);
    display: flex;
    align-items: center;
    justify-content: flex-end;
    padding-right: 24px;
    gap: 8px;
    color: var(--on-primary);
  }
  .status-bar .clock {
    font-size: 26px;
    font-weight: 500;
    margin-left: 10px;
    letter-spacing: 0.5px;
  }
  .app-bar {
    height: 105px;
    background: var(--app-bar);
    display: flex;
    align-items: center;
    padding-left: 32px;
    color: var(--on-primary);
  }
  .app-bar .menu-icon { width: 38px; height: 38px; }
  .app-bar .title {
    margin-left: 36px;
    font-size: 32px;
    font-weight: 700;
    letter-spacing: 0.2px;
  }
  .notification-list { list-style: none; }
  .notification {
    height: 157.5px;
    padding: 34px 30px 0;
  }
  .notification .message {
    font-size: 25.5px;
    line-height: 40px;
    height: 80px;
    overflow: hidden;
    font-weight: 500;
    color: var(--text-unread);
  }
  .notification.is-read .message {
    font-weight: 400;
    color: var(--text-read);
  }
  .notification .time {
    display: block;
    font-size: 22px;
    line-height: 42px;
    color: var(--text-time);
  }
</style>
</head>
<body>
<div class="screen">
  <div class="status-bar">
    <svg width="34" height="28" viewBox="0 0 34 28" aria-hidden="true">
      <path d="M17 27 L0 6 Q17 -6 34 6 Z" fill="currentColor"/>
    </svg>
    <svg width="28" height="28" viewBox="0 0 28 28" aria-hidden="true">
      <path d="M28 0 V28 H0 Z" fill="currentColor"/>
    </svg>
    <svg width="16" height="30" viewBox="0 0 16 30" aria-hidden="true">
      <rect x="5" y="0" width="6" height="3" fill="currentColor"/>
      <rect x="0" y="3" width="16" height="27" rx="1.5" fill="currentColor"/>
    </svg>
    <span class="clock">12:30</span>
  </div>

  <header class="app-bar">
    <svg class="menu-icon" viewBox="0 0 38 38" aria-label="Menu" role="img">
      <rect x="2" y="8" width="34" height="4" fill="currentColor"/>
      <rect x="2" y="17" width="34" height="4" fill="currentColor"/>
      <rect x="2" y="26" width="34" height="4" fill="currentColor"/>
    </svg>
    <h1 class="title">Notifications</h1>
  </header>

  <ul class="notification-list">
    <li class="notification">
      <p class="message">Your Lift-Lantern session Leg Day is ready, three sets of squats and lunges added</p>
      <span class="time">12.30 PM</span>
    </li>
    <li class="notification">
      <p class="message">Sam shared the session Upper Body Push with you, open it to add your own sets</p>
      <span class="time">12.30 PM</span>
    </li>
    <li class="notification">
      <p class="message">Bench press is 80% complete, one more set to finish today's session</p>
      <span class="time">12.30 PM</span>
    </li>
    <li class="notification is-read">
      <p class="message">Reminder: your Full Body session starts at 6 pm, all sets and exercises saved</p>
      <span class="time">12.30 PM</span>
    </li>
    <li class="notification is-read">
      <p class="message">New exercises are ready to choose, try deadlift variations in your next set</p>
      <span class="time">12.30 PM</span>
    </li>
  </ul>
</div>
</body>
</html>
```